Bramblecrest Roofing Co. business card design

I am a Roofing contractor in Texas. The name of my company is Bramblecrest Roofing Co. I also offer a few other services (Christmas light installation, gutters, fencing, pressure washing). However my main gig is roofing. Storm restoration and knowledge of the insurance claim process is my specialty.

My colors are black, red and white. I’d like something pretty simple and clean. Modern looking but with a splash of this red tartan pattern.

I have another version of my logo being edited at the moment where the little top part of the F in roofing that’s currently tartan will be changed to just solid red to make it more visible. So if that’s something you can change in your mock up great. But I can provide the full version once the contest is complete

Target Market(s)

Homeowners

Industry/Entity Type

Roofing

Contact Information for Business Card

Darren Pike. 682-555-0193. www.bramblecrest roofing.example Darren@bramblecrestroofing.example

Colors
EB3D1F
EC4F4E
F09395
F8D3D4
FCEDEE

Requirements
Nice to have
• Maybe instead of a business address. I could say serving all DFW Texas or something like that. And maybe add a line somewhere saying deductible assistance? Just a thought

```html
<!DOCTYPE html>
<html lang="en">
<head>
<meta charset="utf-8">
<title>Bramblecrest Roofing Co. – Business Card</title>
<link href="https://fonts.googleapis.com/css2?family=Michroma&family=Oswald:wght@400;500&family=Poppins:wght@400;700&display=swap" rel="stylesheet">
<style>
  :root {
    --red: #e4151f;
    --black: #111111;
    --ink: #1a1a1a;
    --white: #ffffff;
    --stage: #3a3a3a;
    --emboss: #1f1f1f;
    --divider: #b9b9b9;
  }
  * { margin: 0; padding: 0; box-sizing: border-box; }
  html, body { width: 1200px; height: 689px; overflow: hidden; background: var(--stage); }
  .canvas { position: relative; width: 1200px; height: 689px; }

  .card {
    position: absolute; top: 184px; width: 560px; height: 320px;
    border-radius: 18px; overflow: hidden;
  }
  .card--back { left: 30px; background: var(--black); }
  .card--front { left: 610px; background: var(--white); }

  /* Back side */
  .back-brand {
    position: absolute; left: 0; top: 0; width: 100%; height: 100%;
    display: flex; flex-direction: column; align-items: center; justify-content: center; gap: 14px;
  }
  .back-brand__mark { width: 110px; height: 110px; border-radius: 50%; background: var(--emboss); }
  .back-brand__name {
    font-family: "Poppins", sans-serif; font-weight: 700; font-size: 26px; line-height: 1.05;
    color: var(--emboss); text-align: center; letter-spacing: 1px; text-transform: uppercase;
  }

  /* Front side */
  .brand { position: absolute; left: 18px; top: 34px; width: 226px; display: flex; flex-direction: column; align-items: center; }
  .brand__mark { width: 104px; height: 104px; border-radius: 50%; background: var(--red); }
  .brand__name {
    margin-top: 12px; font-family: "Poppins", sans-serif; font-weight: 700; font-size: 20px;
    line-height: 1.1; color: var(--red); text-align: center; text-transform: uppercase; letter-spacing: .5px;
  }
  .divider { position: absolute; left: 258px; top: 34px; width: 1px; height: 166px; background: var(--divider); }

  .contact { position: absolute; left: 276px; right: 26px; top: 52px; }
  .contact__name {
    font-family: "Michroma", sans-serif; font-size: 18px; color: var(--red);
    text-transform: uppercase; letter-spacing: 1px; white-space: nowrap;
  }
  .contact__list { list-style: none; margin-top: 22px; }
  .contact__item {
    display: flex; align-items: center; gap: 7px; margin-bottom: 7px; white-space: nowrap;
    font-family: "Poppins", sans-serif; font-size: 11.5px; color: var(--ink);
  }
  .contact__icon { width: 12px; height: 12px; flex: none; }

  .band { position: absolute; left: 0; top: 0; width: 560px; height: 320px; }
  .band__text {
    position: absolute; left: 34px; top: 276px; transform: rotate(-3.5deg); transform-origin: left center;
    font-family: "Oswald", sans-serif; font-weight: 500; font-size: 17px; letter-spacing: .5px;
    color: var(--white); white-space: nowrap; text-transform: uppercase;
  }
  .band__text .accent { color: var(--red); }
  .band__text .sep { margin: 0 10px; }
</style>
</head>
<body>
<main class="canvas">

  <section class="card card--back" aria-label="Card back">
    <div class="back-brand">
      <div class="back-brand__mark"></div>
      <p class="back-brand__name">Bramblecrest<br>Roofing Co.</p>
    </div>
  </section>

  <section class="card card--front" aria-label="Card front">
    <svg class="band" viewBox="0 0 560 320" aria-hidden="true">
      <polygon points="0,264 560,222 560,320 0,320" fill="var(--black)"/>
      <polygon points="0,258 560,214 560,219 0,263" fill="var(--red)"/>
      <circle cx="505" cy="218" r="29" fill="var(--white)"/>
      <circle cx="505" cy="218" r="24" fill="none" stroke="var(--red)" stroke-width="3"/>
      <circle cx="505" cy="218" r="18" fill="var(--black)"/>
    </svg>

    <div class="brand">
      <div class="brand__mark"></div>
      <p class="brand__name">Bramblecrest<br>Roofing Co.</p>
    </div>

    <div class="divider"></div>

    <div class="contact">
      <h1 class="contact__name">Darren Pike</h1>
      <ul class="contact__list">
        <li class="contact__item">
          <svg class="contact__icon" viewBox="0 0 24 24"><path fill="var(--red)" d="M6.6 10.8a15.1 15.1 0 0 0 6.6 6.6l2.2-2.2c.3-.3.7-.4 1-.2 1.1.4 2.3.6 3.6.6.6 0 1 .4 1 1V20c0 .6-.4 1-1 1A17 17 0 0 1 3 4c0-.6.4-1 1-1h3.5c.6 0 1 .4 1 1 0 1.3.2 2.5.6 3.6.1.3 0 .7-.2 1l-2.3 2.2z"/></svg>
          682-555-0193
        </li>
        <li class="contact__item">
          <svg class="contact__icon" viewBox="0 0 24 24"><path fill="var(--red)" d="M2 5h20v14H2z"/><path fill="none" stroke="var(--white)" stroke-width="1.8" d="M2 5l10 8 10-8"/></svg>
          Darren@bramblecrestroofing.example
        </li>
        <li class="contact__item">
          <svg class="contact__icon" viewBox="0 0 24 24"><circle cx="12" cy="12" r="10" fill="var(--red)"/><path fill="none" stroke="var(--white)" stroke-width="1.4" d="M2 12h20M12 2c3 3 3 17 0 20M12 2c-3 3-3 17 0 20"/></svg>
          www.bramblecrestroofing.example
        </li>
      </ul>
    </div>

    <p class="band__text"><span class="accent">Serving all DFW Texas</span><span class="sep">|</span>Deductible assistance?</p>
  </section>

</main>
</body>
</html>
```